Harbor Fresh Cleaning car wrap

I need a car wrap design for my work van that is eye catching and stands out. My type of business is carpet cleaning and tile and grout cleaning along with other services. I would like the services to be listed on the wrap along with the phone number and website.
Also please add that we service Commercial and Residential.
Website is:
HarborFreshCleaning.com
Phone number (555) 203-4619
The services I provide are as follow:
Tile & Grout Cleaning
Carpet Cleaning
Hardwood Floor Cleaning and Refinishing
Upholstery and Rug Cleaning
My business colors consist of blue and white but I am open to using other colors.
My logo is attached in the files.
Commercial and Residential
Carpet Cleaning

```html
<!DOCTYPE html>
<html lang="en">
<head>
<meta charset="utf-8">
<title>Harbor Fresh Cleaning – Van Wrap</title>
<link href="https://fonts.googleapis.com/css2?family=Oswald:wght@700&family=Montserrat:wght@600;700;800&display=swap" rel="stylesheet">
<style>
  :root {
    --bg: #eeeff0;
    --van-white: #ffffff;
    --van-line: #c9ced3;
    --skirt: #3a3d42;
    --tire: #26282c;
    --rim: #b9bec4;
    --teal: #1aa39a;
    --teal-light: #5fc8bf;
    --blue: #1f7fb0;
    --ink: #141414;
    --brand-ink: #1f4450;
    --glass: #d7dde2;
    --tail: #c8202a;
    --swoosh: #d9dde1;
  }
  html, body {
    margin: 0;
    width: 1200px;
    height: 1200px;
    overflow: hidden;
    background: radial-gradient(circle at 50% 45%, #f7f8f8 0%, var(--bg) 75%);
  }
  .wrap-sheet { display: block; width: 1200px; height: 1200px; }
  .brand-name { font-family: "Oswald", "Arial Narrow", sans-serif; font-weight: 700; fill: var(--brand-ink); }
  .brand-est { font-family: "Montserrat", Arial, sans-serif; font-weight: 700; fill: #555; letter-spacing: 0.5px; }
  .phone { font-family: "Montserrat", Arial, sans-serif; font-weight: 800; fill: var(--ink); }
  .web { font-family: "Montserrat", Arial, sans-serif; font-weight: 700; fill: #fff; }
  .service { font-family: "Montserrat", Arial, sans-serif; font-weight: 700; fill: #fff; }
  .tagline { font-family: "Montserrat", Arial, sans-serif; font-weight: 700; fill: var(--ink); }
  .panel-line { fill: none; stroke: var(--van-line); stroke-width: 1.5; }
  .body-outline { stroke: #9aa1a8; stroke-width: 1.5; }
  .service-icon { fill: var(--teal-light); opacity: 0.7; }
</style>
</head>
<body>
<svg class="wrap-sheet" viewBox="0 0 1024 1024" xmlns="http://www.w3.org/2000/svg">
  <defs>
    <linearGradient id="wave-grad" x1="0" y1="0" x2="1" y2="0">
      <stop offset="0" stop-color="var(--teal)"/>
      <stop offset="0.55" stop-color="var(--teal)"/>
      <stop offset="1" stop-color="var(--blue)"/>
    </linearGradient>
    <linearGradient id="wave-grad-rev" x1="1" y1="0" x2="0" y2="0">
      <stop offset="0" stop-color="var(--teal)"/>
      <stop offset="0.5" stop-color="var(--teal)"/>
      <stop offset="1" stop-color="var(--blue)"/>
    </linearGradient>
    <linearGradient id="rear-grad" x1="0" y1="0" x2="0" y2="1">
      <stop offset="0" stop-color="var(--teal-light)"/>
      <stop offset="1" stop-color="var(--blue)"/>
    </linearGradient>
    <clipPath id="top-body">
      <path d="M60,398 L56,340 Q58,300 82,286 L182,236 Q232,180 290,130 Q322,100 400,93 L900,88 Q934,88 940,120 L958,290 L966,398 Q966,420 948,420 L64,420 Z"/>
    </clipPath>
    <clipPath id="bottom-body">
      <path d="M60,872 L58,610 Q60,560 110,552 L600,548 Q640,550 660,600 L660,872 Q660,885 645,885 L72,885 Q60,885 60,872 Z"/>
    </clipPath>
    <clipPath id="rear-body">
      <path d="M620,880 L620,600 Q622,560 660,550 L925,550 Q962,560 964,600 L964,880 Z"/>
    </clipPath>
  </defs>

  <!-- ===== Top van: driver side ===== -->
  <g class="van van-side-left">
    <ellipse cx="512" cy="462" rx="450" ry="11" fill="#9a9ea3" opacity="0.55"/>
    <path class="body-outline" fill="var(--van-white)" d="M60,398 L56,340 Q58,300 82,286 L182,236 Q232,180 290,130 Q322,100 400,93 L900,88 Q934,88 940,120 L958,290 L966,398 Q966,420 948,420 L64,420 Z"/>
    <g clip-path="url(#top-body)">
      <path fill="url(#wave-grad)" d="M40,350 Q180,300 400,318 Q590,330 690,240 Q790,140 980,95 L980,430 L40,430 Z"/>
      <path fill="var(--swoosh)" opacity="0.8" d="M620,300 Q720,200 800,140 Q870,100 960,96 L960,112 Q870,118 810,160 Q730,220 650,300 Z"/>
      <path fill="#fff" opacity="0.35" d="M120,330 Q280,300 420,318 Q300,312 130,345 Z"/>
      <rect x="40" y="352" width="940" height="80" fill="var(--skirt)"/>
      <rect x="395" y="386" width="320" height="26" fill="var(--blue)"/>
    </g>
    <path fill="#e8ecef" stroke="#9aa1a8" d="M78,300 L140,285 L135,318 Q100,322 80,318 Z"/>
    <path fill="var(--glass)" stroke="#6b7178" stroke-width="2" d="M210,248 L300,158 L386,155 L386,248 Z"/>
    <path fill="#cfd6dc" stroke="#6b7178" stroke-width="2" d="M188,238 L240,185 L240,240 Z"/>
    <path class="panel-line" d="M195,350 L195,250 M392,140 L392,296 M636,92 L636,350"/>
    <rect class="panel-line" x="425" y="140" width="470" height="115" rx="14"/>
    <rect x="360" y="282" width="28" height="6" rx="3" fill="#555"/>
    <rect x="930" y="250" width="20" height="95" rx="4" fill="var(--tail)"/>

    <text class="brand-name" x="535" y="205" font-size="30" text-anchor="middle">HARBOR FRESH</text>
    <text class="brand-name" x="535" y="232" font-size="20" text-anchor="middle">CLEANING</text>
    <text class="brand-est" x="535" y="247" font-size="7" text-anchor="middle">EST. 2010</text>

    <text class="phone" x="425" y="334" font-size="30" text-anchor="middle">(555) 203-4619</text>
    <text class="web" x="552" y="405" font-size="16" text-anchor="middle">HarborFreshCleaning.com</text>

    <g transform="rotate(-8 770 280)">
      <text class="service" x="690" y="245" font-size="15">• Tile &amp; Grout Cleaning</text>
      <text class="service" x="700" y="267" font-size="15">• Carpet Cleaning</text>
      <text class="service" x="690" y="289" font-size="15">• Hardwood Floor</text>
      <text class="service" x="680" y="309" font-size="15">Cleaning &amp; Refinishing</text>
      <text class="service" x="665" y="331" font-size="15">• Upholstery &amp; Rug Cleaning</text>
    </g>
    <rect class="service-icon" x="624" y="284" width="30" height="32" rx="4" role="img" aria-label="Floor cleaning tool icon"/>
    <rect class="service-icon" x="884" y="262" width="26" height="26" rx="4" role="img" aria-label="Rolled rug icon"/>

    <g class="wheel">
      <circle cx="205" cy="412" r="58" fill="var(--skirt)"/>
      <circle cx="205" cy="412" r="50" fill="var(--tire)"/>
      <circle cx="205" cy="412" r="30" fill="var(--rim)" stroke="#8d939a" stroke-width="3"/>
      <circle cx="205" cy="412" r="9" fill="#7c8289"/>
    </g>
    <g class="wheel">
      <circle cx="792" cy="412" r="58" fill="var(--skirt)"/>
      <circle cx="792" cy="412" r="50" fill="var(--tire)"/>
      <circle cx="792" cy="412" r="30" fill="var(--rim)" stroke="#8d939a" stroke-width="3"/>
      <circle cx="792" cy="412" r="9" fill="#7c8289"/>
    </g>
  </g>

  <!-- ===== Bottom van: passenger side ===== -->
  <g class="van van-side-right">
    <ellipse cx="360" cy="908" rx="300" ry="10" fill="#9a9ea3" opacity="0.55"/>
    <path class="body-outline" fill="var(--van-white)" d="M60,872 L58,610 Q60,560 110,552 L600,548 Q640,550 660,600 L660,872 Q660,885 645,885 L72,885 Q60,885 60,872 Z"/>
    <g clip-path="url(#bottom-body)">
      <path fill="url(#wave-grad-rev)" d="M40,600 Q120,570 220,600 Q330,640 420,720 Q520,800 680,800 L680,900 L40,900 Z"/>
      <path fill="var(--swoosh)" opacity="0.8" d="M70,580 Q200,560 310,620 Q250,590 70,596 Z"/>
      <rect x="40" y="818" width="640" height="80" fill="var(--skirt)"/>
      <rect x="315" y="852" width="330" height="28" fill="var(--blue)"/>
    </g>
    <path class="panel-line" d="M390,555 L390,768 M390,804 L390,818"/>
    <rect class="panel-line" x="118" y="600" width="485" height="115" rx="14"/>
    <rect x="580" y="742" width="28" height="6" rx="3" fill="#555"/>
    <rect x="66" y="715" width="20" height="100" rx="4" fill="var(--tail)"/>

    <text class="brand-name" x="508" y="665" font-size="30" text-anchor="middle">HARBOR FRESH</text>
    <text class="brand-name" x="508" y="692" font-size="20" text-anchor="middle">CLEANING</text>
    <text class="brand-est" x="508" y="706" font-size="7" text-anchor="middle">EST. 2010</text>

    <text class="service" x="155" y="705" font-size="16" transform="rotate(7 155 705)">• Tile &amp; Grout Cleaning</text>
    <text class="service" x="175" y="727" font-size="16" transform="rotate(7 175 727)">• Carpet Cleaning</text>
    <text class="service" x="117" y="760" font-size="16" transform="rotate(7 117 760)">• Hardwood Floor Cleaning &amp; Refinishing</text>
    <text class="service" x="132" y="786" font-size="16" transform="rotate(7 132 786)">• Upholstery &amp; Rug Cleaning</text>
    <rect class="service-icon" x="100" y="710" width="30" height="30" rx="4" role="img" aria-label="Floor cleaning tool icon"/>
    <rect class="service-icon" x="332" y="736" width="28" height="22" rx="4" role="img" aria-label="Rolled rug icon"/>

    <text class="web" x="480" y="872" font-size="17" text-anchor="middle">HarborFreshCleaning.com</text>

    <g class="wheel">
      <circle cx="237" cy="858" r="58" fill="var(--skirt)"/>
      <circle cx="237" cy="858" r="50" fill="var(--tire)"/>
      <circle cx="237" cy="858" r="30" fill="var(--rim)" stroke="#8d939a" stroke-width="3"/>
      <circle cx="237" cy="858" r="9" fill="#7c8289"/>
    </g>
  </g>

  <!-- ===== Rear view ===== -->
  <g class="van van-rear">
    <ellipse cx="790" cy="935" rx="165" ry="10" fill="#9a9ea3" opacity="0.55"/>
    <rect x="628" y="880" width="40" height="50" rx="6" fill="var(--tire)"/>
    <rect x="916" y="880" width="40" height="50" rx="6" fill="var(--tire)"/>
    <path class="body-outline" fill="var(--van-white)" d="M620,880 L620,600 Q622,560 660,550 L925,550 Q962,560 964,600 L964,880 Z"/>
    <g clip-path="url(#rear-body)">
      <rect x="645" y="612" width="294" height="125" rx="12" fill="var(--glass)" stroke="#9aa1a8"/>
      <path fill="url(#wave-grad)" d="M600,700 Q700,760 800,730 Q880,700 980,690 L980,900 L600,900 Z"/>
      <path fill="var(--van-white)" d="M600,735 Q720,790 830,760 Q900,740 980,740 L980,800 Q880,800 800,800 L600,800 Z"/>
      <path fill="var(--teal-light)" opacity="0.6" d="M600,760 Q720,800 840,775 Q760,800 600,775 Z"/>
      <rect x="600" y="800" width="380" height="80" fill="url(#rear-grad)"/>
    </g>
    <rect x="748" y="550" width="56" height="6" rx="2" fill="var(--tail)"/>
    <path class="panel-line" d="M792,556 L792,584 M792,606 L792,644 M792,704 L792,790 M792,818 L792,838"/>
    <circle cx="777" cy="720" r="10" fill="#4a4e54"/>
    <rect x="785" y="770" width="28" height="6" rx="3" fill="#555"/>
    <rect x="620" y="730" width="16" height="100" rx="3" fill="var(--tail)"/>
    <rect x="948" y="730" width="16" height="100" rx="3" fill="var(--tail)"/>
    <rect x="618" y="868" width="348" height="24" rx="6" fill="var(--skirt)"/>

    <text class="tagline" x="777" y="600" font-size="12.5" text-anchor="middle">Serving Commercial &amp; Residential</text>

    <text class="brand-name" x="770" y="665" font-size="24" text-anchor="middle">HARBOR FRESH</text>
    <text class="brand-name" x="770" y="686" font-size="16" text-anchor="middle">CLEANING</text>
    <text class="brand-est" x="770" y="698" font-size="6" text-anchor="middle">EST. 2010</text>

    <text class="brand-name" x="872" y="768" font-size="9" text-anchor="middle">HARBOR FRESH</text>
    <text class="brand-name" x="872" y="778" font-size="7" text-anchor="middle">CLEANING</text>

    <text class="phone" x="826" y="812" font-size="21" text-anchor="middle">(555) 203-4619</text>
    <text class="web" x="777" y="855" font-size="15.5" text-anchor="middle">HarborFreshCleaning.com</text>
  </g>
</svg>
</body>
</html>
```